Business Card Design

We are a business based in Sydney repairing and restoring timber windows. We mainly cater to residential home owners although sometimes work with larger building companies. We do a lot of work in heritage buildings though also cater to modern windows.
Our Logo is Black and Gold and were thinking of using a white card with only these two colours although we are open to any design suggestions. Check out our website for ideas.
Front of Card
Contact Information, Website & Business Name
Back of Card
Business Logo, website?
Target Market(s)
Home Owners
Industry/Entity Type
Residential
Contact Information for Business Card
Oakridge Sash Revivals
Marcus Pellow
0472 309 648
marcus@oakridgesashrevivals.example
www.oakridgesashrevivals.example
Look and feel

```html
<!DOCTYPE html>
<html lang="en">
<head>
<meta charset="utf-8">
<title>Oakridge Sash Revivals — Business Card</title>
<link rel="stylesheet" href="https://fonts.googleapis.com/css2?family=Open+Sans:wght@400&display=swap">
<style>
  :root {
    --page: #e8e6e3;
    --card-light: #ffffff;
    --card-edge: #d6d6d6;
    --banner: #5c5c5c;
    --banner-top: #4a4a4a;
    --ink: #111111;
    --text-grey: #5a5a5a;
    --faint: #c9c9c9;
    --rule: #b9b9b9;
    --track: #e2e2e2;
    --yellow: #f9d53e;
    --blue: #6aafdf;
    --purple: #b462a6;
    --black: #2f2f2f;
  }
  html, body {
    margin: 0;
    width: 1200px;
    height: 1200px;
    overflow: hidden;
    background: var(--page);
    font-family: "Open Sans", Arial, sans-serif;
  }
  .sheet {
    width: 1200px;
    height: 1200px;
    display: flex;
    flex-direction: column;
    align-items: center;
    justify-content: center;
    gap: 60px;
  }
  .card {
    width: 900px;
    height: 520px;
    display: block;
    box-shadow: 0 6px 18px rgba(0,0,0,0.18);
  }
  .card text { font-family: "Open Sans", Arial, sans-serif; font-weight: 400; }
  .name { fill: #ffffff; font-size: 31px; }
  .contact { fill: var(--text-grey); font-size: 22px; }
  .wordmark { fill: var(--ink); font-size: 23px; }
  .wordmark-faint { fill: var(--faint); font-size: 62px; }
  .site { fill: var(--text-grey); font-size: 21px; }
  .icon { fill: none; stroke: var(--text-grey); stroke-width: 1.6; }
  .rule { stroke: var(--rule); stroke-width: 2; }
  .track { fill: var(--track); }
  .s-yellow { fill: var(--yellow); }
  .s-blue { fill: var(--blue); }
  .s-purple { fill: var(--purple); }
  .s-black { fill: var(--black); }
</style>
</head>
<body>
<main class="sheet">

  <!-- Front -->
  <svg class="card card-front" viewBox="0 0 900 520" xmlns="http://www.w3.org/2000/svg">
    <defs>
      <radialGradient id="paper-front" cx="0.45" cy="0.55" r="0.75">
        <stop offset="0" stop-color="var(--card-light)"/>
        <stop offset="1" stop-color="var(--card-edge)"/>
      </radialGradient>
    </defs>
    <rect width="900" height="520" fill="url(#paper-front)"/>

    <g class="name-banner">
      <polygon points="0,132 360,132 330,186 0,186" fill="var(--banner)"/>
      <polygon points="0,132 360,132 354,142 0,142" fill="var(--banner-top)"/>
      <text class="name" x="62" y="174">Marcus Pellow</text>
    </g>

    <g class="contacts">
      <circle class="icon" cx="54" cy="228" r="10"/>
      <path class="icon" d="M49,223 q0,10 10,10 l2,-3 -3,-2 -2,2 q-4,-2 -5,-5 l2,-2 -2,-3 z"/>
      <text class="contact" x="76" y="236">0472 309 648</text>

      <circle class="icon" cx="54" cy="262" r="10"/>
      <rect class="icon" x="48" y="258" width="12" height="8"/>
      <path class="icon" d="M48,258 l6,5 6,-5"/>
      <text class="contact" x="76" y="270">marcus@oakridgesashrevivals.example</text>

      <circle class="icon" cx="54" cy="296" r="10"/>
      <ellipse class="icon" cx="54" cy="296" rx="4.5" ry="10"/>
      <line class="icon" x1="44" y1="296" x2="64" y2="296"/>
      <text class="contact" x="76" y="304">www.oakridgesashrevivals.example</text>
    </g>

    <line class="rule" x1="640" y1="0" x2="360" y2="520"/>

    <g class="wordmark-block">
      <text class="wordmark" x="600" y="222">Oakridge</text>
      <text class="wordmark" x="600" y="250">Sash</text>
      <text class="wordmark" x="600" y="278">Revivals</text>
    </g>

    <g class="stripe-band">
      <polygon class="track" points="441,370 900,370 900,476 384,476"/>
      <polygon class="s-yellow" points="470,385 585,385 545,460 430,460"/>
      <polygon class="s-blue" points="585,385 700,385 660,460 545,460"/>
      <polygon class="s-purple" points="700,385 815,385 775,460 660,460"/>
      <polygon class="s-black" points="815,385 900,385 900,460 775,460"/>
    </g>
  </svg>

  <!-- Back -->
  <svg class="card card-back" viewBox="0 0 900 520" xmlns="http://www.w3.org/2000/svg">
    <defs>
      <radialGradient id="paper-back" cx="0.5" cy="0.5" r="0.75">
        <stop offset="0" stop-color="var(--card-light)"/>
        <stop offset="1" stop-color="var(--card-edge)"/>
      </radialGradient>
    </defs>
    <rect width="900" height="520" fill="url(#paper-back)"/>

    <g class="faint-name">
      <text class="wordmark-faint" x="55" y="130">Oakridge</text>
      <text class="wordmark-faint" x="75" y="205">Sash</text>
      <text class="wordmark-faint" x="95" y="280">Revivals</text>
    </g>

    <line class="rule" x1="620" y1="0" x2="330" y2="520"/>

    <g class="wordmark-block">
      <text class="wordmark" x="590" y="270">Oakridge</text>
      <text class="wordmark" x="590" y="298">Sash</text>
      <text class="wordmark" x="590" y="326">Revivals</text>
    </g>

    <text class="site" x="868" y="410" text-anchor="end">www.oakridgesashrevivals.example</text>

    <g class="stripe-band">
      <rect class="track" x="0" y="430" width="900" height="90"/>
      <polygon class="s-yellow" points="-35,440 90,440 55,505 -70,505"/>
      <polygon class="s-blue" points="90,440 215,440 180,505 55,505"/>
      <polygon class="s-purple" points="215,440 340,440 305,505 180,505"/>
      <polygon class="s-black" points="340,440 465,440 430,505 305,505"/>
      <polygon class="s-yellow" points="465,440 590,440 555,505 430,505"/>
      <polygon class="s-blue" points="590,440 715,440 680,505 555,505"/>
      <polygon class="s-purple" points="715,440 840,440 805,505 680,505"/>
      <polygon class="s-black" points="840,440 965,440 930,505 805,505"/>
    </g>
  </svg>

</main>
</body>
</html>
```